BRAVOLK PROMOTION GROUP Website

Looking for a website design that clearly and powerfully portrays our unique and effective indoor advertising billboards in our network.

Our TeenyPanels, LargoPanels and TitanFlags are strategically placed in high traffic areas of restaurants, pubs, nightclubs, fitness clubs, colleges and universities, and sports arenas.

Bravolk Promotion Group is our new name. Our current site is www.plorvex.ca with our focus now being entirely on our Out-of-Home media. New website address will be www.bravolkpromotion.ca

We need the following sections:

HOME
PRODUCTS (Drop down menu)
-TeenyPanels
-LargoPanels
-TitanFlags
NETWORKS (Drop down menu)
-Resto-Bar
-Sports
-Campus
EFFECTIVENESS
CAMPAIGNS *This page will show numerous ad campaigns and could be a slide show (see www.plorvex.ca/QJPV_campaigns.html )
BECOME A PARTNER
CONTACT

Please include social media functions on the homepage such as chirpnet/visagebook/workloop

We will be supplying content and photos as required.

Our plan is to have you submit the homepage design to start with, and then we can start judging which styles we like the best and can start narrowing our list. As a second round, we would like to ask the "finalists" to submit a second page (another section of the website) and to see how consistent you are in terms of the look and feel you proposed for the homepage.

Attached is our new logo.

We may require you to upload the final website for us.

Websites that are in similar industry are:
www.trelmuk.com
www.quasplen.com

Industry/Entity Type

Advertising

Requirements
Must have
• Our network offers advertising solutions that feature: Guaranteed Readership,100% Gender Specific, Frequency, and Captive Audience. Purchasing advertising space in our network are small to medium business owners and advertising agencies booking on behalf of their clients.

Site must be professional and modern looking.
Nice to have
• Moving banner or slide show of some type.

```html
<!DOCTYPE html>
<html lang="en">
<head>
<meta charset="utf-8">
<title>Bravolk Promotion Group</title>
<link rel="stylesheet" href="https://fonts.googleapis.com/css2?family=Ubuntu:wght@400;500;700&family=Arimo:wght@400;700&display=swap">
<style>
  :root {
    --blue: #2f6db5;
    --blue-light: #4a8ad6;
    --blue-dark: #1f559b;
    --ink: #1d1d1d;
    --grey-text: #333333;
    --page-top: #ffffff;
    --page-bottom: #e2e2e2;
    --nav-active: #8a8a8a;
    --box-top: #9d9d9d;
    --box-bottom: #6d6d6d;
    --white: #ffffff;
  }
  * { margin: 0; padding: 0; box-sizing: border-box; }
  html, body { width: 1200px; height: 860px; overflow: hidden; }
  body {
    position: relative;
    background: linear-gradient(180deg, var(--page-top) 0%, var(--page-top) 12%, var(--page-bottom) 100%);
    font-family: "Arimo", Arial, sans-serif;
    color: var(--ink);
  }
  .brand {
    position: absolute; left: 46px; top: 34px;
    display: flex; align-items: center; gap: 12px;
  }
  .brand-mark {
    width: 54px; height: 54px; border-radius: 10px;
    background: var(--blue);
  }
  .brand-name {
    font-family: "Ubuntu", sans-serif; font-weight: 700;
    font-size: 26px; line-height: 1.05; color: var(--blue);
    letter-spacing: 0.5px; width: 200px;
  }
  .social {
    position: absolute; right: 78px; top: 92px;
    display: flex; gap: 12px; list-style: none;
  }
  .social li {
    display: flex; align-items: center; gap: 4px;
    font-family: "Ubuntu", sans-serif; font-size: 12px; color: var(--blue-dark);
  }
  .social li::before {
    content: ""; width: 14px; height: 14px; background: var(--blue); display: block;
  }
  .main-nav {
    position: absolute; left: 34px; top: 138px; width: 1131px; height: 48px;
    background: linear-gradient(180deg, var(--blue-light) 0%, var(--blue) 55%, var(--blue-dark) 100%);
    border-radius: 4px; box-shadow: 0 1px 3px rgba(0,0,0,.3);
  }
  .main-nav ul { list-style: none; display: flex; height: 100%; padding-left: 24px; }
  .main-nav li {
    font-family: "Ubuntu", sans-serif; font-weight: 500; font-size: 17px;
    color: var(--white); padding: 0 21px; display: flex; align-items: center;
  }
  .main-nav li.active {
    background: linear-gradient(180deg, #a8a8a8, var(--nav-active));
  }
  .slider {
    position: absolute; left: 40px; top: 205px; width: 1120px; height: 337px;
    background: var(--white); border-radius: 4px;
    box-shadow: 0 1px 4px rgba(0,0,0,.25);
  }
  .slide-title {
    position: absolute; left: 34px; top: 22px;
    font-family: "Ubuntu", sans-serif; font-size: 37px; color: var(--ink); font-weight: 400;
  }
  .benefits { position: absolute; left: 42px; top: 74px; list-style: none; }
  .benefits li {
    font-family: "Ubuntu", sans-serif; font-size: 21px; color: var(--ink);
    display: flex; align-items: center; gap: 10px; height: 36px;
  }
  .cta-button {
    position: absolute; left: 30px; top: 247px; width: 212px; height: 53px;
    background: linear-gradient(180deg, var(--blue-light), var(--blue-dark));
    border-radius: 3px; color: var(--white);
    font-family: "Ubuntu", sans-serif; font-size: 21px;
    display: flex; align-items: center; padding-left: 22px;
  }
  .slide-presenter {
    position: absolute; left: 440px; top: 59px; width: 340px; height: 278px;
    background: linear-gradient(180deg, #f1ece8 0%, #c9b2a2 45%, #2a2a30 100%);
  }
  .slide-venue {
    position: absolute; left: 812px; top: 10px; width: 263px; height: 319px;
    background: linear-gradient(180deg, #9aa4ac 0%, #6a6f72 50%, #3a3b3c 100%);
  }
  .slide-arrow { position: absolute; top: 340px; width: 40px; height: 40px; }
  .slide-arrow.prev { left: 25px; }
  .slide-arrow.next { left: 1136px; }
  .intro {
    position: absolute; left: 46px; top: 574px; width: 748px;
    font-size: 14.2px; line-height: 18px; color: var(--grey-text);
  }
  .intro p + p { margin-top: 18px; }
  .venues {
    position: absolute; top: 691px; list-style: none;
    font-weight: 700; font-size: 15.5px; letter-spacing: 0.6px; color: var(--ink);
  }
  .venues li { display: flex; align-items: center; gap: 9px; height: 22px; }
  .venues li::before {
    content: ""; border-left: 9px solid #666; border-top: 6px solid transparent;
    border-bottom: 6px solid transparent;
  }
  .venues.col-a { left: 70px; }
  .venues.col-b { left: 290px; top: 695px; }
  .call-box {
    position: absolute; left: 817px; top: 569px; width: 331px; height: 172px;
    background: linear-gradient(180deg, var(--box-top), var(--box-bottom));
    border: 1px solid #5a5a5a; border-radius: 4px;
    box-shadow: 0 1px 3px rgba(0,0,0,.3);
    color: var(--white); font-family: "Ubuntu", sans-serif; padding: 14px 0 0 22px;
  }
  .call-box .call-title { font-weight: 700; font-size: 22px; letter-spacing: 0.3px; }
  .call-box .call-label { font-size: 19px; margin-top: 10px; }
  .call-box .call-phone { font-weight: 700; font-size: 27px; margin-top: 14px; }
  .site-footer {
    position: absolute; left: 0; top: 814px; width: 1200px; height: 46px;
    background: var(--blue);
    color: var(--white); font-size: 12.5px;
    display: flex; align-items: center; justify-content: flex-end; padding-right: 50px;
  }
</style>
</head>
<body>
  <header>
    <div class="brand">
      <span class="brand-mark"></span>
      <span class="brand-name">Bravolk Promotion Group</span>
    </div>
    <ul class="social">
      <li>visagebook</li>
      <li>chirpnet</li>
      <li>workloop</li>
    </ul>
    <nav class="main-nav">
      <ul>
        <li class="active">HOME</li>
        <li>PRODUCTS</li>
        <li>NETWORKS</li>
        <li>EFFECTIVENESS</li>
        <li>CAMPAIGNS</li>
        <li>BECOME A PARTNER</li>
        <li>CONTACT</li>
      </ul>
    </nav>
  </header>

  <section class="slider">
    <h1 class="slide-title">Lorem ipsum dolor sit amet</h1>
    <ul class="benefits">
      <li><svg width="16" height="14" viewBox="0 0 16 14"><path d="M1 8 L5 12 L15 1" fill="none" stroke="#1d1d1d" stroke-width="2.6"/></svg>Guaranteed Readership</li>
      <li><svg width="16" height="14" viewBox="0 0 16 14"><path d="M1 8 L5 12 L15 1" fill="none" stroke="#1d1d1d" stroke-width="2.6"/></svg>100% Gender Specific</li>
      <li><svg width="16" height="14" viewBox="0 0 16 14"><path d="M1 8 L5 12 L15 1" fill="none" stroke="#1d1d1d" stroke-width="2.6"/></svg>Frequency</li>
      <li><svg width="16" height="14" viewBox="0 0 16 14"><path d="M1 8 L5 12 L15 1" fill="none" stroke="#1d1d1d" stroke-width="2.6"/></svg>Captive Audience</li>
    </ul>
    <div class="cta-button">Start your ad campaign</div>
    <div class="slide-presenter" role="img" aria-label="Photo of a businesswoman pointing toward an indoor advertising panel"></div>
    <div class="slide-venue" role="img" aria-label="Photo of an advertising panel mounted on a pillar at a busy street location"></div>
  </section>
  <svg class="slide-arrow prev" viewBox="0 0 40 40" aria-label="Previous slide"><circle cx="20" cy="20" r="18" fill="#2f6db5" stroke="#ffffff" stroke-width="2"/><path d="M24 10 L14 20 L24 30" fill="none" stroke="#ffffff" stroke-width="5"/></svg>
  <svg class="slide-arrow next" viewBox="0 0 40 40" aria-label="Next slide"><circle cx="20" cy="20" r="18" fill="#2f6db5" stroke="#ffffff" stroke-width="2"/><path d="M16 10 L26 20 L16 30" fill="none" stroke="#ffffff" stroke-width="5"/></svg>

  <main>
    <div class="intro">
      <p>Lorem ipsum dolor sit amet, has et ponderum deterruisset, quo porro accusam at, no paulo eleifend ocurreret duo. Vide audire ocurreret in est. Mei reque corpora at, ne eligendi facilisis vix, et vis putant interpretaris. No nec porro adipisci, sit nibh erat senserit no. Ferri accusamus mediocritatem vim at.</p>
      <p>Our TeenyPanels, LargoPanels and TitanFlags are strategically placed in high traffic areas of:</p>
    </div>
    <ul class="venues col-a">
      <li>Restaurants</li>
      <li>Pubs</li>
      <li>Nightclubs</li>
    </ul>
    <ul class="venues col-b">
      <li>Fitness clubs</li>
      <li>Colleges and universities</li>
      <li>Sports arenas.</li>
    </ul>
    <aside class="call-box">
      <div class="call-title">START YOUR AD CAMPAIGN</div>
      <div class="call-label">CALL US</div>
      <div class="call-phone">555-014-7732</div>
    </aside>
  </main>

  <footer class="site-footer">Copyright 2012 Bravolk Promotion Group</footer>
</body>
</html>
```